Bertucci Estates Wine flyer

We have imported 4 wines and need a brochure that talks about them as well as some info about the winery they come from.

Target Market(s)

Wine drinkers; young professionals

Colors
ec1f27
9bcb3c
3176b5
f78f20

Requirements
Must have
• Wine elements - vintage look
Should not have
• Clipart look

```html
<!DOCTYPE html>
<html lang="en">
<head>
<meta charset="utf-8">
<title>Bertucci Estates – Tri-fold Brochure</title>
<link rel="stylesheet" href="https://fonts.googleapis.com/css2?family=Jost:wght@400;500;700&display=swap">
<style>
  :root {
    --backdrop: #e4e4e4;
    --paper: #ffffff;
    --orange: #f78f20;
    --orange-soft: #fde3c8;
    --green: #9bcb3c;
    --green-soft: #e8f3d3;
    --wine: #4a1c22;
    --wine-deep: #2e1216;
    --ink: #2e2e2e;
    --ink-soft: #555555;
    --rule: #e2d6d0;
  }
  * { box-sizing: border-box; margin: 0; padding: 0; }
  html, body {
    width: 1200px; height: 816px; overflow: hidden;
    background: var(--backdrop);
    font-family: "Jost", "Futura", sans-serif;
    color: var(--ink);
  }
  .brochure {
    position: absolute; left: 60px; top: 128px;
    width: 1080px; height: 560px;
    display: flex;
    box-shadow: 0 10px 30px rgba(0,0,0,.18);
  }
  .panel { position: relative; width: 360px; height: 560px; overflow: hidden; }

  /* Brand name (logo stand-in) */
  .brand {
    display: flex; align-items: center; gap: 8px;
    font-size: 17px; font-weight: 700; color: var(--wine);
  }
  .brand__dot { width: 12px; height: 12px; border-radius: 50%; background: var(--wine); flex: none; }

  /* About panel */
  .panel--about {
    background: linear-gradient(180deg, var(--orange) 0%, #f9ae63 35%, var(--orange-soft) 62%, var(--paper) 80%);
  }
  .about { padding: 56px 30px 0; }
  .about__title { font-size: 17px; font-weight: 700; margin-bottom: 6px; }
  .about__body { font-size: 12.5px; line-height: 1.38; text-align: justify; font-weight: 500; }
  .panel__photo-bottom { position: absolute; left: 0; bottom: 0; width: 360px; height: 200px; }

  /* Contact panel */
  .panel--contact {
    background: linear-gradient(180deg, var(--green) 25%, #c4e08c 48%, var(--green-soft) 72%, var(--paper) 92%);
  }
  .panel__photo-top { position: absolute; left: 0; top: 0; width: 360px; height: 150px; }
  .panel--contact .brand { position: absolute; top: 200px; left: 0; right: 0; justify-content: center; }
  .contact { position: absolute; top: 262px; left: 30px; right: 20px; }
  .contact__title { font-size: 22px; font-weight: 700; color: var(--orange); margin-bottom: 4px; }
  .contact__people { font-size: 12px; line-height: 1.35; color: var(--ink-soft); margin-bottom: 10px; }
  .contact__phone { font-size: 12px; color: var(--ink-soft); margin-bottom: 8px; }
  .contact__web { font-size: 15px; font-weight: 700; margin-bottom: 8px; }
  .contact__email { font-size: 12px; color: var(--ink-soft); }

  /* Cover panel */
  .panel--cover { background: var(--paper); }
  .panel--cover .brand { position: absolute; top: 26px; left: 30px; }
  .cover__photo { position: absolute; left: 30px; top: 70px; width: 300px; height: 290px; }
  .wines { position: absolute; left: 30px; right: 30px; top: 380px; }
  .wines__title { font-size: 15px; font-weight: 700; color: var(--orange); margin-bottom: 8px; }
  .wines__list { list-style: none; }
  .wine {
    display: flex; justify-content: space-between; align-items: baseline;
    padding: 6px 0; border-bottom: 1px solid var(--rule);
    font-size: 12.5px;
  }
  .wine__name { font-weight: 700; color: var(--wine); }
  .wine__type { color: var(--ink-soft); font-weight: 400; }
</style>
</head>
<body>
  <main class="brochure">
    <section class="panel panel--about">
      <div class="about">
        <h2 class="about__title">About Us:</h2>
        <p class="about__body">Bertucci produces quality wines with grapes coming exclusively from its own vineyards. The vineyard's agronomic techniques are targeted and carried out manually. The meticulous process of choosing and picking of the grapes, the traditional winemaking techniques and a cellar, stocked with every technical device, leads to the production of top-tier wines that are an expression of the territory Piceno and their passion for this craft that has been handed down for three generations. Vigneti Bertucci was birthed in 1963 when Giulia Marconi and Enzo Bertucci decided to dedicate their future to the land and wine that he loved as a child. Prior to 1963 the family Marconi had chosen the path of oil and wine. The first harvest and olive oil production of the family Marconi can be traced to the year 1905.</p>
      </div>
      <svg class="panel__photo-bottom" viewBox="0 0 360 200" role="img" aria-label="Photo of a vineyard terrace with garden chairs and mountains behind">
        <defs>
          <linearGradient id="vineyardTones" x1="0" y1="0" x2="0" y2="1">
            <stop offset="0" stop-color="#4b5d3a"/>
            <stop offset=".35" stop-color="#8fb0d3"/>
            <stop offset=".6" stop-color="#6f9350"/>
            <stop offset="1" stop-color="#3f6e2a"/>
          </linearGradient>
        </defs>
        <path d="M0 70 Q180 -30 360 70 L360 200 L0 200 Z" fill="url(#vineyardTones)"/>
        <path d="M0 70 Q180 -30 360 70" fill="none" stroke="var(--orange)" stroke-width="6"/>
      </svg>
    </section>

    <section class="panel panel--contact">
      <svg class="panel__photo-top" viewBox="0 0 360 150" role="img" aria-label="Photo of green grape bunches in harvest crates">
        <defs>
          <linearGradient id="grapeTones" x1="0" y1="0" x2="1" y2="1">
            <stop offset="0" stop-color="#6f8c6a"/>
            <stop offset=".5" stop-color="#c7d98a"/>
            <stop offset="1" stop-color="#9fbf4c"/>
          </linearGradient>
        </defs>
        <path d="M0 0 H360 V80 Q180 190 0 80 Z" fill="url(#grapeTones)"/>
        <path d="M0 80 Q180 190 360 80" fill="none" stroke="var(--orange)" stroke-width="5"/>
      </svg>
      <div class="brand"><span class="brand__dot"></span>Bertucci Estates</div>
      <div class="contact">
        <h2 class="contact__title">Contact</h2>
        <p class="contact__people">Paolo Renzi, Chief Executive Officer<br>Clara Mendes, Chief Operating Officer</p>
        <p class="contact__phone">555.014.2207</p>
        <p class="contact__web">www.bertucciestates.com</p>
        <p class="contact__email">Sales@BertucciEstates.com</p>
      </div>
    </section>

    <section class="panel panel--cover">
      <div class="brand"><span class="brand__dot"></span>Bertucci Estates</div>
      <svg class="cover__photo" viewBox="0 0 300 290" role="img" aria-label="Photo of a red wine bottle with a bunch of dark grapes and vine leaves">
        <defs>
          <linearGradient id="bottleTones" x1="0" y1="0" x2="0" y2="1">
            <stop offset="0" stop-color="#f4f7ef"/>
            <stop offset=".35" stop-color="#a9c97a"/>
            <stop offset=".7" stop-color="var(--wine)"/>
            <stop offset="1" stop-color="var(--wine-deep)"/>
          </linearGradient>
        </defs>
        <rect x="0" y="0" width="300" height="290" rx="14" fill="url(#bottleTones)"/>
      </svg>
      <div class="wines">
        <h2 class="wines__title">Our Imported Wines</h2>
        <ul class="wines__list">
          <li class="wine"><span class="wine__name">Rosso Piceno 2019</span><span class="wine__type">Red</span></li>
          <li class="wine"><span class="wine__name">Montepulciano Riserva 2018</span><span class="wine__type">Red</span></li>
          <li class="wine"><span class="wine__name">Pecorino Colline 2021</span><span class="wine__type">White</span></li>
          <li class="wine"><span class="wine__name">Falerio Bianco 2021</span><span class="wine__type">White</span></li>
        </ul>
      </div>
    </section>
  </main>
</body>
</html>
```